BRETON CAPITAL INSTITUTIONAL PRESENTATION

To create a powerpoint presentation with selected art and text.
Target Market(s)
Potential Investors for the fund
Industry/Entity Type
Finance
Font styles to use
Sans Serif
Colors
0692cd
0255a3
Requirements
Must have
- Unique art, to look sober and professional
Nice to have
- Modern look
Should not have
- Red as color...

```html
<!DOCTYPE html>
<html lang="en">
<head>
<meta charset="utf-8">
<title>Breton Capital – Institutional Presentation</title>
<link href="https://fonts.googleapis.com/css2?family=Lato:wght@300;400;700&display=swap" rel="stylesheet">
<style>
:root{
  --ink:#3a4548;
  --muted:#6e7679;
  --sky:#45b8f2;
  --blue:#1582c8;
  --navy:#0e5d8f;
  --slate:#7b8b8c;
  --steel:#4a5659;
  --char:#2b3335;
  --band:#1a7bc8;
  --band-light:#4a9be8;
  --line:#3a3f41;
}
*{margin:0;padding:0;box-sizing:border-box}
html,body{width:1200px;height:1200px;overflow:hidden;background:#fff}
body{position:relative;font-family:"Lato",Helvetica,Arial,sans-serif;color:var(--ink)}
.slide{position:absolute;left:88px;width:1024px;height:577px;background:#fff;box-shadow:2px 3px 5px rgba(0,0,0,.45)}
.slide--model{top:11px}
.slide--fund{top:606px}
.abs{position:absolute}
.brand-corner{position:absolute;right:22px;top:30px;display:flex;align-items:center;gap:6px;font-size:11px;font-weight:400;color:var(--navy);letter-spacing:.5px}
.brand-corner .dot{width:12px;height:12px;border-radius:50%;background:var(--blue)}
.slide-title{position:absolute;left:0;width:1024px;top:40px;text-align:center;font-weight:300;font-size:36px;font-variant:small-caps;letter-spacing:1px;color:var(--ink)}
.rule{position:absolute;height:1.5px;width:46px;background:var(--band)}
.subtitle{position:absolute;left:0;width:1024px;top:97px;text-align:center;font-size:14px;font-weight:300}
.steps-list .item{position:absolute;left:54px;display:flex;align-items:center;height:44px;margin-top:-22px}
.steps-list .num{width:24px;font-size:23px;font-weight:700;color:var(--ink)}
.steps-list .text{font-size:11.5px;line-height:14.4px;font-weight:400;color:#444}
.node{position:absolute;width:120px;height:120px;border-radius:50%;margin:-60px 0 0 -60px;display:flex;align-items:center;justify-content:center;text-align:center;padding:0 14px;color:#fff;font-size:10px;line-height:12.8px;font-weight:300}
.step-label{position:absolute;font-size:23px;font-weight:700;color:var(--ink);transform:translate(-50%,-50%)}
.center-note{position:absolute;left:498px;width:340px;top:320px;text-align:center;font-size:12.5px;line-height:15px;color:#777;font-weight:300}
.flow{position:absolute;left:0;top:0}
.footer-band{position:absolute;left:0;width:1024px;top:542px;height:6px;background:var(--band)}
.slide--fund .footer-band{background:var(--band-light)}
.footer-meta{position:absolute;left:46px;top:553px;font-size:10px;color:#555;letter-spacing:.3px}
.footer-brand{position:absolute;left:0;width:1024px;top:551px;text-align:center;font-size:16px;font-weight:400;color:var(--char);letter-spacing:.5px}
.page-no{position:absolute;left:952px;top:553px;width:24px;text-align:center;font-size:10px;color:#555}
.facts .fact{position:absolute;left:138px;width:443px;display:flex;align-items:center;justify-content:center;text-align:center;padding:0 60px;color:#fff;font-size:12px;line-height:15.5px;font-weight:300}
.fund-title{position:absolute;left:658px;top:250px;font-size:38px;line-height:47px;font-weight:300;font-variant:small-caps;letter-spacing:1px;color:var(--ink)}
.fund-sub{position:absolute;left:660px;top:364px;font-size:19px;font-weight:300;color:var(--ink)}
</style>
</head>
<body>

<section class="slide slide--model">
  <div class="brand-corner"><span class="dot"></span>BRETON CAPITAL</div>
  <h1 class="slide-title">Breton Capital</h1>
  <div class="rule" style="left:489px;top:89px"></div>
  <p class="subtitle">A unique investment model</p>

  <div class="steps-list">
    <div class="item" style="top:144px"><span class="num">1.</span><p class="text">Lorem ipsum dolor sit amet,<br>consectetuer adipiscing elit.<br>Aenean commodo ligula eget.</p></div>
    <div class="item" style="top:208px"><span class="num">2.</span><p class="text">Lorem ipsum dolor sit amet,<br>consectetuer adipiscing elit.<br>Aenean commodo ligula eget.</p></div>
    <div class="item" style="top:272px"><span class="num">3.</span><p class="text">Lorem ipsum dolor sit amet,<br>consectetuer adipiscing elit.<br>Aenean commodo ligula eget.</p></div>
    <div class="item" style="top:336px"><span class="num">4.</span><p class="text">Lorem ipsum dolor sit amet,<br>consectetuer adipiscing elit.<br>Aenean commodo ligula eget.</p></div>
    <div class="item" style="top:400px"><span class="num">5.</span><p class="text">Lorem ipsum dolor sit amet,<br>consectetuer adipiscing elit.<br>Aenean commodo ligula eget.</p></div>
    <div class="item" style="top:464px"><span class="num">6.</span><p class="text">Lorem ipsum dolor sit amet,<br>consectetuer adipiscing elit.<br>Aenean commodo ligula eget.</p></div>
  </div>

  <svg class="flow" width="1024" height="577" viewBox="0 0 1024 577" fill="none" stroke="var(--line)" stroke-width="1">
    <defs>
      <marker id="head" markerWidth="8" markerHeight="8" refX="7" refY="4" orient="auto">
        <path d="M1 1 L7 4 L1 7" fill="none" stroke="#3a3f41" stroke-width="1"/>
      </marker>
    </defs>
    <polyline points="405,274 405,216 486,216" marker-end="url(#head)"/>
    <polyline points="618,216 690,216" marker-end="url(#head)"/>
    <polyline points="822,214 918,214 918,269" marker-end="url(#head)"/>
    <polyline points="918,395 918,454 824,454" marker-end="url(#head)"/>
    <polyline points="690,454 618,454" marker-end="url(#head)"/>
    <polyline points="486,454 405,454 405,401" marker-end="url(#head)"/>
  </svg>

  <div class="node" style="left:553px;top:218px;background:var(--navy)">Lorem ipsum dolor sit amet, consectetuer adipiscing elit. Aenean commodo ligula eget dolor.</div>
  <div class="node" style="left:758px;top:218px;background:var(--blue)">Lorem ipsum dolor sit amet, consectetuer adipiscing elit. Aenean commodo ligula eget dolor.</div>
  <div class="node" style="left:918px;top:334px;background:var(--sky)">Lorem ipsum dolor sit amet, consectetuer adipiscing elit. Aenean commodo ligula eget dolor.</div>
  <div class="node" style="left:758px;top:451px;background:var(--slate)">Lorem ipsum dolor sit amet, consectetuer adipiscing elit. Aenean commodo ligula eget dolor.</div>
  <div class="node" style="left:553px;top:451px;background:var(--steel)">Lorem ipsum dolor sit amet, consectetuer adipiscing elit. Aenean commodo ligula eget dolor.</div>
  <div class="node" style="left:409px;top:334px;background:var(--char)">Lorem ipsum dolor sit amet, consectetuer adipiscing elit. Aenean commodo ligula eget dolor.</div>

  <span class="step-label" style="left:469px;top:194px">1.</span>
  <span class="step-label" style="left:674px;top:194px">2.</span>
  <span class="step-label" style="left:940px;top:259px">3.</span>
  <span class="step-label" style="left:832px;top:434px">4.</span>
  <span class="step-label" style="left:629px;top:436px">5.</span>
  <span class="step-label" style="left:387px;top:409px">6.</span>

  <p class="center-note">Lorem ipsum dolor sit amet, consectetuer adipiscing elit. Aenean commodo ligula eget dolor</p>

  <div class="footer-band"></div>
  <p class="footer-meta">DATE &nbsp;|&nbsp; LOREM IPSUM</p>
  <p class="footer-brand">BRETON CAPITAL</p>
  <p class="page-no">14</p>
</section>

<section class="slide slide--fund">
  <div class="brand-corner"><span class="dot"></span>BRETON CAPITAL</div>

  <svg class="flow" width="1024" height="577" viewBox="0 0 1024 577" fill="none" stroke="var(--line)" stroke-width="1">
    <polyline points="138,136 46,136 46,475 138,475"/>
    <polyline points="581,136 607,136 607,475 581,475"/>
  </svg>

  <div class="facts">
    <div class="fact" style="top:106px;height:62px;background:var(--sky)">This new offshore vehicle is Breton Capital’s only fund that is open to investors</div>
    <div class="fact" style="top:174px;height:61px;background:var(--blue)">Capacity is capped at $500 million</div>
    <div class="fact" style="top:241px;height:61px;background:var(--navy)">Volatility of new fund is targeted at 12</div>
    <div class="fact" style="top:308px;height:62px;background:var(--slate)">Brazilian asset manager with proven understanding of Emerging Markets</div>
    <div class="fact" style="top:375px;height:61px;background:var(--steel)">20 months of fund data shows Breton Capital can generate alpha in the macro area</div>
    <div class="fact" style="top:442px;height:61px;background:var(--char)">In contrast, Meridian Macro Index up 1.6% in 2018; many top managers in drawdown</div>
  </div>

  <h2 class="fund-title">Breton Macro<br>Global Fund</h2>
  <div class="rule" style="left:662px;top:351px"></div>
  <p class="fund-sub">The Opportunity</p>

  <div class="footer-band"></div>
  <p class="footer-meta">DATE &nbsp;|&nbsp; LOREM IPSUM</p>
  <p class="footer-brand">BRETON CAPITAL</p>
  <p class="page-no">13</p>
</section>

</body>
</html>
```